Book Cover for Memoir: Sexual Assault and Traumatic Stress

I need a cover design for a memoir that is a victim's story of a sexual assault. I will need a print-on-demand cover, an eBook cover, and a 3D thumbnail image. The thumbnail and eBook cover will be used immediately, and the POD cover will be used in a few months with the full manuscript is ready. Therefore, I need an artist who is willing to make small adjustments if needed once the page count is set.

I have a image I have purchased that should give you an idea of the desired direction, but you can feel free to use your own images. I have attached some examples of book covers I like. I attached a color palette for fonts.

Overall Look: Fonts should be feminine and thin, but large to stand out. Look should be simple and elegant, and display and overall depressing feeling. There should be enough detail though to make it look professionally put together. Not TOO minimalistic.

I have also attached the Paper Loom templates if you choose to use those. If not, ensure there is an open place for the barcode on the bottom right.

Requirements
Must have
• Title: Beneath Quiet Rooms
Subtitle: A Daughter's Record of Silence, Doubt & Mending
Author: Nora Jean Whitfield
Audience: Mostly women 18-30
Quote (for the back): "I always thought I'd know how I'd react if I ever was raped. I was wrong. I've been wrong a lot lately."
Summary (back cover): When twenty-seven-year-old Nora Whitfield wakes up with a gut-wrenching feeling, she has little memory of the horrifying events that occurred the night before. Days earlier, Nora was a spirited single mom who had abandoned her hometown to raise her daughter in the city and pursue her dreams. In the short months since Nora’s move to Seattle, she became the adored lover of a charismatic lawyer, started a new business, and finally felt life was going her way. So what happened to cause her to break?

In a gripping and heartbreaking narrative, Nora tells the true story of how her life unraveled from the traumatic events that took place that night and why what seems obvious to everyone else is impossible for Nora to believe. Beneath Quiet Rooms is a chilling exploration of memory through trauma, trust in humanity, and a captivating story of strength and survival that appeals to the heart of fathers and mothers, sons and daughters, and men and women alike.
Nice to have
• BACK COVER: I'd like to have a photo on the back. This should depict the happy life of the main character before the sexual assault, and should be with her daughter. Or should be a nature scene that starts at the corner and blends into the rest of the cover. I have attached a possible image or you can use something you like.

```html
<!DOCTYPE html>
<html lang="en">
<head>
<meta charset="utf-8">
<title>Beneath Quiet Rooms — Full Cover</title>
<link href="https://fonts.googleapis.com/css2?family=Raleway:wght@200;300;400;600&display=swap" rel="stylesheet">
<style>
  :root {
    --paper: #ffffff;
    --back-top: #2b1b15;
    --back-bottom: #170d0a;
    --teal: #3fc1b2;
    --text-light: #efe7e2;
    --text-muted: #cfc3bc;
    --barcode-box: #e9e0df;
    --skin-light: #e3c6b6;
    --skin-mid: #c49a87;
    --hair-dark: #24170f;
  }
  * { box-sizing: border-box; margin: 0; padding: 0; }
  html, body {
    width: 1200px; height: 854px; overflow: hidden;
    background: var(--paper);
    font-family: "Raleway", "Helvetica Neue", sans-serif;
  }
  .cover {
    position: absolute; left: 0; top: 10px;
    width: 1200px; height: 830px;
  }
  /* Back cover */
  .back {
    position: absolute; left: 0; top: 0; width: 557px; height: 830px;
    background: linear-gradient(180deg, var(--back-top), var(--back-bottom));
  }
  .back-photo {
    position: absolute; left: 66px; top: 28px; width: 423px; height: 245px;
    border: 5px solid var(--paper);
    background: linear-gradient(180deg, #cfe2f1 0%, #e9eef0 40%, #9aa7a0 62%, #b8977c 82%, #8a6a52 100%);
  }
  .summary {
    position: absolute; left: 70px; width: 475px;
    color: var(--text-light);
    font-size: 12.4px; line-height: 15.6px; font-weight: 300;
  }
  .summary--intro { top: 285px; }
  .summary--intro::first-letter { font-size: 17px; }
  .summary--close { top: 562px; font-size: 12px; }
  .rule {
    position: absolute; left: 130px; width: 300px; height: 1px;
    background: linear-gradient(90deg, transparent, rgba(255,255,255,0.45), transparent);
  }
  .rule--top { top: 420px; }
  .rule--bottom { top: 538px; }
  .pull-quote {
    position: absolute; left: 40px; top: 440px; width: 480px;
    text-align: center; text-transform: uppercase;
    color: var(--text-muted); font-weight: 200;
    font-size: 19px; line-height: 23px; letter-spacing: 1px;
  }
  .pull-quote .bright { color: var(--paper); font-weight: 300; }
  .pull-quote .accent { color: var(--teal); font-weight: 300; }
  .barcode-space {
    position: absolute; left: 351px; top: 690px; width: 185px; height: 98px;
    background: var(--barcode-box);
  }
  /* Spine + front share the photo */
  .front-photo {
    position: absolute; left: 557px; top: 0; width: 643px; height: 830px;
    background:
      linear-gradient(200deg, var(--hair-dark) 0%, rgba(60,40,30,0.85) 22%, rgba(140,105,90,0.3) 45%, transparent 60%),
      linear-gradient(160deg, var(--skin-light) 0%, var(--skin-mid) 55%, #8a6354 100%);
  }
  .spine-title, .spine-author {
    position: absolute; white-space: nowrap;
    transform-origin: left top; transform: rotate(90deg);
  }
  .spine-title {
    left: 616px; top: 42px;
    color: var(--teal); font-size: 30px; font-weight: 200; letter-spacing: 1px;
  }
  .spine-title b { font-weight: 600; }
  .spine-author {
    left: 611px; top: 612px;
    color: var(--paper); font-size: 13px; font-weight: 300; letter-spacing: 2.5px;
  }
  .front-title {
    position: absolute; left: 700px; top: 360px; width: 440px;
    text-align: center; color: var(--paper); text-transform: uppercase;
    line-height: 0.98;
  }
  .front-title .word { display: block; font-size: 72px; font-weight: 200; letter-spacing: 2px; }
  .front-title .word--bold { font-weight: 400; font-size: 78px; }
  .subtitle {
    position: absolute; left: 700px; top: 618px; width: 440px;
    text-align: center; color: var(--paper); text-transform: uppercase;
  }
  .subtitle .lead { display: block; font-size: 19px; font-weight: 300; letter-spacing: 1.5px; }
  .subtitle .tail { display: block; font-size: 12.5px; font-weight: 300; letter-spacing: 1.5px; margin-top: 2px; }
  .front-author {
    position: absolute; left: 660px; top: 778px; width: 520px;
    text-align: center; color: var(--teal); text-transform: uppercase;
    font-size: 30px; font-weight: 300; letter-spacing: 5px;
  }
</style>
</head>
<body>
  <main class="cover">
    <section class="back">
      <div class="back-photo" role="img" aria-label="Photograph of a mother and young daughter sitting on a lakeside dock, feet splashing in the water on a bright day"></div>
      <p class="summary summary--intro">When twenty-seven-year-old Nora Whitfield wakes up with a gut-wrenching feeling, she has little memory of the horrifying events that occurred the night before. Days earlier, Nora was a spirited single mom who had abandoned her hometown to raise her daughter in the city and pursue her dreams. In the short months since Nora’s move to Seattle, she became the adored lover of a charismatic lawyer, started a new business, and finally felt life was going her way. So what happened to cause her to break?</p>
      <div class="rule rule--top"></div>
      <blockquote class="pull-quote">"I always thought I'd know<br>how I'd react <span class="bright">if I ever was raped.</span><br><span class="accent">I was wrong.</span><br>I've been wrong a lot lately."</blockquote>
      <div class="rule rule--bottom"></div>
      <p class="summary summary--close">In a gripping and heartbreaking narrative, Nora tells the true story of how her life unraveled from the traumatic events that took place that night and why what seems obvious to everyone else is impossible for Nora to believe. Beneath Quiet Rooms is a chilling exploration of memory through trauma, trust in humanity, and a captivating story of strength and survival that appeals to the heart of fathers and mothers, sons and daughters, and men and women alike.</p>
      <div class="barcode-space"></div>
    </section>

    <div class="front-photo" role="img" aria-label="Close-up portrait photograph of a young woman with dark hair resting her chin on her hand, gazing at the viewer"></div>

    <h2 class="spine-title">BENEATH <b>QUIET</b> ROOMS</h2>
    <p class="spine-author">NORA JEAN WHITFIELD</p>

    <section class="front">
      <h1 class="front-title">
        <span class="word">Beneath</span>
        <span class="word word--bold">Quiet</span>
        <span class="word">Rooms</span>
      </h1>
      <p class="subtitle">
        <span class="lead">A Daughter's Record</span>
        <span class="tail">of Silence, Doubt &amp; Mending</span>
      </p>
      <p class="front-author">Nora Jean Whitfield</p>
    </section>
  </main>
</body>
</html>
```